Personal Injury Funding Flyer

We are Qorvale Financial, a provider of receivables management solutions to the surgical industry.
We want a 1 page flyer to showcase our Motor Vehicle Accident (MVA) and Personal Injury (PI) case management and lien purchasing.

Attached is a document:
1- a flyer from a competitor. We like the overall feel of the flyer and the simplicity of the information presented.

You can also check out our website for examples of our company's style
www.qorvalefinancial.example

Target Market(s)

Surgeons, office managers, administrators and CFOS at smaller surgical facilities and surgical hospitals nationwide

Industry/Entity Type

Financial

Requirements
Must have
• Titled: Personal Injury Case Funding
• Tagline: We Ensure Your Cases are Financially Sound
• Include Qorvale Financial's logo
• Be sure to boldly highlight the 3 points:
• 3 Steps to Successful PI Case Management
• 1) Evaluate Cases
• Evaluate the financial aspects of the case including policy limits.
• 2) Consult Attorneys
• Evaluate the case background and likelihood of settlement.
• 3) Guaranteed Funding
• 15 day funding on most cases.
• How Does MVA/PI Funding Work?
• We pay you upfront and wait for the case to settle.
• Our funding eliminates the risk, hassle and uncertainty associated with PI cases.
• You get paid 100% NON-RECOURSE
• Include contact phone number (800) 555-0147
• >No Hassles
• >No Risk
• >Guaranteed Funds.
Nice to have
• Smiling doctor picture
Should not have
• Too much information

```html
<!DOCTYPE html>
<html lang="en">
<head>
<meta charset="utf-8">
<title>Qorvale Financial – Personal Injury Case Funding</title>
<link rel="stylesheet" href="https://fonts.googleapis.com/css2?family=Roboto+Condensed:wght@300;700&family=Roboto:wght@700&family=Oswald:wght@600&family=Open+Sans:wght@600;700&display=swap">
<style>
  :root {
    --page-bg: #e4e4e4;
    --ink-dark: #1c1f24;
    --maroon: #5a0f0f;
    --navy: #0f1238;
    --cyan: #4fd2f5;
    --yellow: #f5e21a;
    --white: #ffffff;
    --gray-box: #8a8a8a;
    --text-dark: #2a2a2a;
  }
  html, body {
    margin: 0;
    padding: 0;
    width: 909px;
    height: 1200px;
    overflow: hidden;
    background: var(--page-bg);
  }
  .flyer {
    position: absolute;
    left: 62px;
    top: 57px;
    width: 780px;
    height: 1083px;
    background: var(--white);
    overflow: hidden;
    box-shadow: 0 2px 10px rgba(0,0,0,0.25);
    font-family: "Open Sans", sans-serif;
  }
  .backdrop { position: absolute; left: 0; top: 0; }
  .photo { position: absolute; }
  .photo-team-top {
    left: 380px; top: 33px; width: 400px; height: 345px;
    background: linear-gradient(180deg, #3a3f46 0%, #e9ecef 55%, #cfd8dc 100%);
  }
  .photo-stethoscope {
    left: 478px; top: 493px; width: 247px; height: 185px;
    background: radial-gradient(ellipse at 55% 50%, #b5322c 0%, #d9a29e 40%, #ffffff 72%);
  }
  .photo-team-bottom {
    left: 0; top: 868px; width: 500px; height: 215px;
    background: linear-gradient(180deg, #ffffff 0%, #eef1f3 40%, #dde3e8 100%);
  }
  .logo-tab {
    position: absolute; left: 25px; top: 0; width: 268px; height: 98px;
    background: var(--white);
    border-radius: 0 0 20px 20px;
  }
  .logo-name {
    position: absolute; left: 14px; top: 34px;
    display: flex; align-items: center; gap: 7px;
    font-family: "Roboto Condensed", sans-serif; font-weight: 700;
    font-size: 19px; color: var(--ink-dark); white-space: nowrap;
  }
  .logo-mark { width: 12px; height: 12px; background: var(--maroon); }
  .logo-divider {
    position: absolute; left: 196px; top: 26px; width: 1px; height: 48px;
    background: #b9b9b9;
  }
  .logo-tagline {
    position: absolute; left: 203px; top: 29px;
    font-family: "Roboto Condensed", sans-serif; font-weight: 700;
    font-size: 11.5px; line-height: 14px; color: var(--maroon);
  }
  .logo-tagline span:last-child { color: #666; }
  .headline {
    position: absolute; left: 25px; top: 152px; margin: 0;
    font-weight: 700; text-transform: uppercase; white-space: nowrap;
  }
  .headline-accent {
    display: block; font-family: "Roboto Condensed", sans-serif;
    font-size: 52px; line-height: 52px; color: var(--cyan);
    transform: scaleX(0.85); transform-origin: left;
  }
  .headline-main {
    display: block; font-family: "Roboto", sans-serif;
    font-size: 48px; line-height: 46px; color: var(--white);
  }
  .tagline {
    position: absolute; left: 25px; top: 244px; margin: 0;
    font-family: "Roboto Condensed", sans-serif; font-weight: 300;
    font-size: 19.5px; color: var(--cyan); white-space: nowrap;
  }
  .company-note {
    position: absolute; left: 0; width: 780px; top: 400px; margin: 0;
    text-align: center;
    font-family: "Roboto Condensed", sans-serif; font-weight: 700;
    font-size: 10.6px; color: var(--yellow); text-transform: uppercase;
  }
  .phone {
    position: absolute; left: 486px; top: 428px;
    display: flex; align-items: center; gap: 8px;
    font-family: "Roboto Condensed", sans-serif; font-weight: 700;
    font-size: 36px; color: var(--white);
  }
  .steps-title {
    position: absolute; left: 25px; top: 452px; margin: 0;
    font-family: "Oswald", sans-serif; font-weight: 600;
    font-size: 27px; color: var(--navy); letter-spacing: -0.6px;
    text-transform: uppercase; white-space: nowrap;
    transform: scaleX(0.86); transform-origin: left;
  }
  .steps-title .step-count { color: var(--maroon); font-size: 40px; }
  .steps { position: absolute; left: 25px; top: 505px; margin: 0; padding: 0; list-style: none; }
  .step { position: relative; height: 47px; padding-left: 32px; white-space: nowrap; }
  .step-number {
    position: absolute; left: 0; top: 2px; width: 22px; height: 36px;
    background: var(--gray-box); color: var(--white);
    font-family: "Roboto", sans-serif; font-size: 17px;
    display: flex; align-items: center; justify-content: center;
  }
  .step:nth-child(2) .step-number { background: var(--navy); }
  .step-name {
    display: block; font-size: 21px; line-height: 24px; font-weight: 600; color: var(--maroon);
  }
  .step-text {
    display: block; font-size: 14px; line-height: 16px; font-weight: 600; color: var(--text-dark);
  }
  .how-title {
    position: absolute; left: 25px; top: 722px; margin: 0;
    font-family: "Roboto Condensed", sans-serif; font-weight: 700;
    font-size: 38px; color: var(--yellow); text-transform: uppercase; white-space: nowrap;
  }
  .how-list { position: absolute; left: 25px; top: 772px; margin: 0; padding: 0; list-style: none; }
  .how-list li {
    position: relative; padding-left: 19px; height: 29px; white-space: nowrap;
    font-size: 18.5px; line-height: 25px; font-weight: 600; color: var(--white);
  }
  .how-list li::before {
    content: ""; position: absolute; left: 0; top: 9px;
    width: 8px; height: 8px; background: var(--cyan);
  }
  .how-list .highlight { color: var(--yellow); }
  .promise {
    position: absolute; right: 22px; top: 926px; margin: 0;
    text-align: right; white-space: nowrap;
  }
  .promise span { display: block; transform-origin: right; }
  .promise-hassles {
    font-family: "Roboto Condensed", sans-serif; font-weight: 700;
    font-size: 54px; line-height: 54px; color: var(--maroon);
    transform: scaleX(0.86);
  }
  .promise-risk {
    font-family: "Roboto", sans-serif; font-weight: 700;
    font-size: 58px; line-height: 54px; color: var(--navy);
    transform: scaleX(0.88);
  }
  .promise-funds {
    font-family: "Roboto Condensed", sans-serif; font-weight: 300;
    font-size: 38px; line-height: 42px; color: var(--maroon);
    transform: scaleX(0.92);
  }
</style>
</head>
<body>
<main class="flyer">
  <svg class="backdrop" width="780" height="1083" viewBox="0 0 780 1083" aria-hidden="true">
    <rect x="0" y="0" width="780" height="385" fill="var(--ink-dark)"/>
    <path d="M0 358 H285 C320 358 318 380 350 380 H780 V483 H470 C440 483 440 443 405 443 H0 Z" fill="var(--maroon)"/>
    <path d="M0 345 H285 C320 345 318 372 350 372 H780" fill="none" stroke="var(--white)" stroke-width="6"/>
    <path d="M0 668 H320 C350 668 352 708 385 708 H780 V918 H520 C490 918 488 878 455 878 H0 Z" fill="var(--navy)"/>
  </svg>

  <div class="photo photo-team-top" role="img" aria-label="Smiling team of doctors in white coats giving a thumbs up"></div>
  <div class="photo photo-stethoscope" role="img" aria-label="Red stethoscope"></div>
  <div class="photo photo-team-bottom" role="img" aria-label="Group of smiling young doctors with stethoscopes"></div>

  <header class="logo-tab">
    <div class="logo-name"><span class="logo-mark"></span>Qorvale Financial</div>
    <div class="logo-divider"></div>
    <div class="logo-tagline"><span>Receivable</span><br><span>Management</span><br><span>Solutions</span></div>
  </header>

  <h1 class="headline">
    <span class="headline-accent">Personal Injury</span>
    <span class="headline-main">Case Funding</span>
  </h1>
  <p class="tagline">We Ensure Your Cases are Financially Sound</p>

  <p class="company-note">Qorvale Financial is a privately-held company that exclusively specializes in collecting receivables for providers of health care.</p>

  <div class="phone">
    <svg width="26" height="26" viewBox="0 0 26 26" aria-hidden="true">
      <rect x="1" y="1" width="24" height="24" rx="5" fill="var(--white)"/>
      <path d="M9 6 C7 7 6 9 7.5 12.5 C9 16 11.5 18.5 14.5 19.5 C17 20.3 18.5 19.5 19.5 18 L17 15.5 L15 16.5 C13 15.5 11 13.5 10 11.5 L11 9.5 Z" fill="var(--maroon)"/>
    </svg>
    <span>800-555-0147</span>
  </div>

  <h2 class="steps-title"><span class="step-count">3</span> Steps to Successful PI Case Management</h2>
  <ol class="steps">
    <li class="step"><span class="step-number">1</span><span class="step-name">Evaluate Cases</span><span class="step-text">Evaluate the financial aspects of the case including policy limits.</span></li>
    <li class="step"><span class="step-number">2</span><span class="step-name">Consult Attorneys</span><span class="step-text">Evaluate the case background and likelihood of settlement.</span></li>
    <li class="step"><span class="step-number">3</span><span class="step-name">Guaranteed Funding</span><span class="step-text">15 day funding on most cases.</span></li>
  </ol>

  <h2 class="how-title">How Does MVA/PI Funding Work?</h2>
  <ul class="how-list">
    <li>We pay you upfront and wait for the case to settle.</li>
    <li>Our funding eliminates the risk, hassle and uncertainty associated with PI cases.</li>
    <li>You get paid <span class="highlight">100%</span> NON-RECOURSE</li>
  </ul>

  <p class="promise">
    <span class="promise-hassles">NO HASSLES</span>
    <span class="promise-risk">NO RISK</span>
    <span class="promise-funds">Guaranteed Funds</span>
  </p>
</main>
</body>
</html>
```